" A Lorquia é uma empresa que tem como maior foco de trabalho executar transformaçoes positivas em equipes de desenvolvimento de software. Portanto três palavras definem nosso trabalho: Evoluçao, Crescimento e Mudança. Para isso nos apoiamos no trabalho em equipe, para potencializar a colaboraçao e motivar as pessoas (principal elemento de um organizaçao). Para conhecer mais nosso trabalho, visite www.lorquia-exemplo.com.br "

```html
<!DOCTYPE html>
<html lang="pt-BR">
<head>
<meta charset="utf-8">
<title>Lorquia — cartão de visita</title>
<link rel="stylesheet" href="https://fonts.googleapis.com/css2?family=Comfortaa:wght@400;600&family=Caveat:wght@400&display=swap">
<style>
  :root {
    --orange: #f26a12;
    --orange-light: #f7923a;
    --ink: #3a3a3a;
    --paper: #ffffff;
    --stage: #e9e7e4;
    --white-soft: rgba(255,255,255,0.92);
  }
  * { box-sizing: border-box; margin: 0; padding: 0; }
  html, body { width: 1200px; height: 1200px; overflow: hidden; }
  body {
    background: var(--stage);
    font-family: "Comfortaa", sans-serif;
    display: flex;
    align-items: center;
    justify-content: center;
    gap: 80px;
  }
  .card {
    width: 480px;
    height: 820px;
    border-radius: 56px;
    position: relative;
    overflow: hidden;
    box-shadow: 0 10px 30px rgba(0,0,0,0.12);
  }

  /* Front */
  .card-front { background: var(--paper); }
  .halftone-area {
    position: absolute;
    top: 0; left: 0; right: 0;
    height: 330px;
    background: linear-gradient(180deg, var(--orange) 0%, var(--orange-light) 35%, rgba(247,146,58,0.35) 70%, rgba(255,255,255,0) 100%);
  }
  .brand {
    position: absolute;
    left: 0; right: 0;
    top: 520px;
    text-align: center;
  }
  .brand-mark {
    width: 64px; height: 64px;
    border-radius: 50%;
    background: var(--orange);
    margin: 0 auto 28px;
  }
  .brand-name {
    font-family: "Comfortaa", sans-serif;
    font-weight: 400;
    font-size: 76px;
    line-height: 1;
    color: var(--ink);
    letter-spacing: 1px;
  }

  /* Back */
  .card-back { background: var(--orange); color: var(--paper); }
  .quote {
    position: absolute;
    top: 70px; left: 50px; right: 50px;
    font-family: "Caveat", cursive;
    font-size: 31px;
    line-height: 1.3;
    text-align: center;
    color: var(--white-soft);
  }
  .quote-author {
    position: absolute;
    top: 300px; right: 56px;
    font-family: "Caveat", cursive;
    font-size: 28px;
    color: var(--white-soft);
  }
  .holder {
    position: absolute;
    left: 50px; top: 470px;
    font-family: "Comfortaa", sans-serif;
    font-weight: 600;
    font-size: 34px;
  }
  .contacts {
    position: absolute;
    left: 50px; top: 540px;
    list-style: none;
  }
  .contact {
    display: flex;
    align-items: center;
    gap: 14px;
    font-size: 21px;
    height: 40px;
    white-space: nowrap;
  }
  .contact-icon {
    width: 26px; height: 26px;
    border-radius: 50%;
    background: var(--paper);
    display: flex; align-items: center; justify-content: center;
    flex: none;
  }
  .contact-icon svg { width: 16px; height: 16px; }
</style>
</head>
<body>
  <section class="card card-front">
    <div class="halftone-area" role="img" aria-label="Padrão decorativo de pontos laranja que se dissolvem em direção ao centro do cartão"></div>
    <div class="brand">
      <div class="brand-mark"></div>
      <div class="brand-name">lorquia</div>
    </div>
  </section>

  <section class="card card-back">
    <p class="quote">“Para sobreviver e ter sucesso, cada organização tem de se tornar um agente de mudança. A forma mais eficaz de gerenciar a mudança é criá-la.”</p>
    <p class="quote-author">Paulo Dantas</p>

    <h1 class="holder">Nome e Sobrenome</h1>
    <ul class="contacts">
      <li class="contact">
        <span class="contact-icon"><svg viewBox="0 0 16 16"><path d="M4 2l2.5 3-1.5 1.5a8 8 0 0 0 4.5 4.5L11 9.5l3 2.5-1.5 2C7 14 2 9 2 3.5z" fill="#f26a12"/></svg></span>
        (11) 5555.0100
      </li>
      <li class="contact">
        <span class="contact-icon"><svg viewBox="0 0 16 16"><rect x="2" y="4" width="12" height="8" rx="1" fill="none" stroke="#f26a12" stroke-width="1.6"/><path d="M2.5 4.5L8 9l5.5-4.5" fill="none" stroke="#f26a12" stroke-width="1.6"/></svg></span>
        nome@lorquia-exemplo.com.br
      </li>
      <li class="contact">
        <span class="contact-icon"><svg viewBox="0 0 16 16"><circle cx="8" cy="8" r="5.5" fill="none" stroke="#f26a12" stroke-width="1.5"/><path d="M2.5 8h11M8 2.5c-2.5 3-2.5 8 0 11M8 2.5c2.5 3 2.5 8 0 11" fill="none" stroke="#f26a12" stroke-width="1.2"/></svg></span>
        www.lorquia-exemplo.com.br
      </li>
      <li class="contact">
        <span class="contact-icon"></span>
        /lorquia
      </li>
      <li class="contact">
        <span class="contact-icon"></span>
        @lorquia
      </li>
    </ul>
  </section>
</body>
</html>
```